Website design for luxury private hair salon

I'm looking for someone to use my Logo and build me a website for my webpage www.corvelstudio.com.au (You can have a look at it as it has every detail I need included on it already), however I want a fresh new appearance and it to look and feel super stylish.

I am thinking colours in black, with silver or white, beautiful hair images like the ones you'll see on the current webpage - the price list as per what you already see.

I will include a copy of my biz card on here, so you can see the feel of the card, and design a website with a similar feel. It is matt black with a foil silver.

Modern, but classic and fresh. I will also need you to be able to publish it to my URL for me as I have no idea how to do this. I need it up and running pronto!

The website will need to be able to be read clearly on all devices incluing smart phones and ipads. The URL is currently registered and hosted by Brindle Serve

Thinking a Home Page - large logo etc and write up on who and what we offer
Services/Price List page - as per the price list on my current webpage
Contact Page - with a built in contact form.

Target Market(s)

Middle aged, fashionable, stylish women and men who enjoy luxury hair care and styling in an upmarket location.

Industry/Entity Type

Hair And Beauty

Number of Pages Required

3 page

Font styles to use
Other font styles liked:
• see my images for my current logo

Colors
000000
b2b2b2
a54499

Requirements
Must have
• Style
• Fast turnaround
• Be viewable on all devices, PC, ipads, smart phones
• Designer able to upload it so its a running website for me to my URL
Nice to have
• Just a really feminine, stylish website which is easy to read and shows some beautiful images of perfect hair
Should not have
• Browns, reds or orange colours.

```html
<!DOCTYPE html>
<html lang="en">
<head>
<meta charset="utf-8">
<title>Corvel – Private Hair Salon</title>
<link href="https://fonts.googleapis.com/css2?family=Open+Sans:wght@400;600;700&family=Lato:wght@300;400;700&display=swap" rel="stylesheet">
<style>
  :root {
    --ink: #1c1b20;
    --nav-bg: #26252b;
    --hero-bg: #2f2e35;
    --hero-soft: #4a4950;
    --plum: #a54499;
    --plum-soft: #c07ab8;
    --paper: #f4f4f5;
    --white: #ffffff;
    --silver: #b2b2b2;
  }
  * { margin: 0; padding: 0; box-sizing: border-box; }
  html, body { width: 1200px; height: 1200px; overflow: hidden; }
  body { background: var(--paper); font-family: "Lato", sans-serif; color: var(--ink); }

  .site { position: relative; width: 1200px; height: 1200px; overflow: hidden; }

  .backdrop { position: absolute; inset: 0; }

  .main-nav {
    position: absolute; top: 0; left: 0; right: 0; height: 92px;
    background: rgba(30, 29, 34, 0.85);
    display: flex; justify-content: center; align-items: stretch;
    padding-left: 120px;
  }
  .main-nav a {
    font-family: "Open Sans", sans-serif; font-weight: 600; font-size: 15px;
    letter-spacing: 0.04em; color: var(--white); text-decoration: none;
    display: flex; align-items: center; padding: 0 22px;
  }
  .main-nav a.is-active { background: var(--plum); }

  .brand-name {
    position: absolute; top: 230px; left: 0; right: 0; text-align: center;
    font-family: "Lato", sans-serif; font-weight: 300; font-size: 118px;
    letter-spacing: 0.14em; color: var(--white); padding-left: 90px;
  }

  .portrait-diamond {
    position: absolute; left: 118px; top: 565px; width: 300px; height: 300px;
    transform: rotate(45deg);
    background: linear-gradient(135deg, var(--plum) 0%, var(--plum-soft) 45%, #5b3a5a 100%);
    box-shadow: 0 12px 30px rgba(0,0,0,0.18);
  }

  .welcome {
    position: absolute; left: 520px; top: 760px; width: 600px; text-align: center;
  }
  .welcome h1 {
    font-family: "Open Sans", sans-serif; font-weight: 700; font-size: 32px;
    letter-spacing: 0.02em; color: var(--ink); margin-bottom: 22px;
  }
  .welcome h1 .accent { color: var(--plum); }
  .welcome p { font-size: 15px; line-height: 1.6; color: #333238; }
  .welcome .signature { margin-top: 18px; font-weight: 700; font-size: 14px; }
</style>
</head>
<body>
<div class="site">
  <svg class="backdrop" width="1200" height="1200" viewBox="0 0 1200 1200" aria-hidden="false">
    <defs>
      <linearGradient id="heroPhoto" x1="0" y1="0" x2="1" y2="0.3">
        <stop offset="0" stop-color="#2d2c33"/>
        <stop offset="0.55" stop-color="#38373e"/>
        <stop offset="0.8" stop-color="#55545b"/>
        <stop offset="1" stop-color="#3c3b42"/>
      </linearGradient>
      <linearGradient id="paperMist" x1="0" y1="0" x2="1" y2="1">
        <stop offset="0" stop-color="#f7f7f8"/>
        <stop offset="1" stop-color="#e9e9ec"/>
      </linearGradient>
    </defs>
    <rect x="0" y="0" width="1200" height="1200" fill="url(#paperMist)"/>
    <polygon points="0,0 1200,0 1200,610 0,660" fill="url(#heroPhoto)" role="img" aria-label="Soft monochrome photo of a woman with styled hair and a fur collar"/>
    <line x1="0" y1="661" x2="1200" y2="611" stroke="var(--plum)" stroke-width="3"/>
  </svg>

  <nav class="main-nav">
    <a href="#" class="is-active">HOME</a>
    <a href="#">SERVICES</a>
    <a href="#">CONTACT</a>
  </nav>

  <div class="brand-name">CORVEL</div>

  <div class="portrait-diamond" role="img" aria-label="Portrait photo of a woman with a sleek bob, toned in plum"></div>

  <section class="welcome">
    <h1>WELCOME TO <span class="accent">CORVEL</span></h1>
    <p>We pride ourselves on being able to offer a private salon experience to our clients in the exclusive suburb of Ashbury Vale, where your hair design and colouring needs will be met with years of experience and current industry training and knowledge".</p>
    <p class="signature">- The Corvel Team -</p>
  </section>
</div>
</body>
</html>
```